Business cards for KORBEN Real Estate Properties LLC

We need a cool, original business card design for a company based in the Washington DC metropolitan area. We are a new energetic and passionate Real Estate Investing Company that invests in all types of real estate; commercial, residential, industrial etc.

Our company color is Red since it reflects action, energy and speed; it is assertive confident, energizing, exciting, powerful, passionate and determined. So we would like business card communicate those qualities to the audience.

Our audiences are investors that want to invest with us, real estate sellers, buyers, and tenants who lease from us.

Our logo is attached

```html
<!DOCTYPE html>
<html lang="en">
<head>
<meta charset="utf-8">
<title>KORBEN Real Estate Properties LLC – Business Cards</title>
<link rel="stylesheet" href="https://fonts.googleapis.com/css2?family=Ubuntu:wght@400;500;700&display=swap">
<style>
  :root {
    --brand-red: #b5182a;
    --brand-red-dark: #9c1424;
    --ink: #222222;
    --ink-soft: #555555;
    --paper: #f7f7f5;
    --stage: #d9d9d9;
    --white: #ffffff;
  }
  * { box-sizing: border-box; margin: 0; padding: 0; }
  html, body {
    width: 1200px;
    height: 1000px;
    overflow: hidden;
    background: var(--stage);
    font-family: "Ubuntu", sans-serif;
  }
  .sheet {
    position: relative;
    width: 1200px;
    height: 1000px;
  }
  .card {
    position: absolute;
    left: 250px;
    width: 700px;
    height: 400px;
    overflow: hidden;
    box-shadow: 0 6px 18px rgba(0,0,0,0.18);
  }
  .card-front { top: 70px; background: var(--paper); }
  .card-back { top: 530px; background: var(--brand-red); }

  .card-bands {
    position: absolute;
    inset: 0;
    width: 100%;
    height: 100%;
  }
  .band-red { fill: var(--brand-red-dark); }
  .band-black { fill: var(--ink); }

  .brand {
    position: absolute;
    left: 190px;
    top: 78px;
    display: flex;
    flex-direction: column;
    align-items: flex-start;
  }
  .brand-row {
    display: flex;
    align-items: center;
    gap: 16px;
  }
  .brand-dot {
    width: 34px;
    height: 34px;
    border-radius: 50%;
    background: var(--brand-red);
  }
  .brand-name {
    font-size: 68px;
    font-weight: 700;
    letter-spacing: 2px;
    color: var(--ink);
    line-height: 1;
  }
  .brand-tagline {
    margin-top: 6px;
    margin-left: 50px;
    font-size: 19px;
    font-weight: 500;
    color: var(--ink);
    letter-spacing: 0.5px;
  }
  .web-address {
    position: absolute;
    right: 40px;
    top: 270px;
    font-size: 19px;
    color: var(--ink-soft);
    letter-spacing: 0.5px;
  }

  .back-band {
    position: absolute;
    left: 0;
    right: 0;
    bottom: 0;
    height: 70px;
    background: var(--ink);
  }
  .contact {
    position: absolute;
    right: 400px;
    top: 112px;
    text-align: right;
    color: var(--white);
    font-size: 19px;
    line-height: 1.15;
  }
  .contact-item { margin-bottom: 12px; }
  .contact-item:last-child { margin-bottom: 0; }
  .contact-icons {
    position: absolute;
    left: 318px;
    top: 130px;
    display: flex;
    flex-direction: column;
    gap: 26px;
  }
  .contact-icon {
    width: 26px;
    height: 26px;
    border-radius: 50%;
    background: var(--white);
    display: flex;
    align-items: center;
    justify-content: center;
  }
  .contact-icon svg { width: 15px; height: 15px; fill: var(--brand-red); }
  .person {
    position: absolute;
    left: 370px;
    top: 140px;
    color: var(--white);
  }
  .person-name {
    font-size: 27px;
    font-weight: 700;
    letter-spacing: 0.5px;
  }
  .person-role {
    font-size: 17px;
    margin-top: 2px;
  }
</style>
</head>
<body>
<main class="sheet">

  <section class="card card-front" aria-label="Business card front">
    <svg class="card-bands" viewBox="0 0 700 400" preserveAspectRatio="none" aria-hidden="true">
      <path class="band-red" d="M0 222 H360 C405 222 412 305 462 305 H700 V320 H0 Z"/>
      <path class="band-black" d="M468 320 H700 V338 H498 C486 338 478 330 468 320 Z"/>
    </svg>
    <div class="brand">
      <div class="brand-row">
        <span class="brand-dot"></span>
        <span class="brand-name">KORBEN</span>
      </div>
      <span class="brand-tagline">REAL ESTATE PROPERTIES LLC</span>
    </div>
    <p class="web-address">www.webaddress.com</p>
  </section>

  <section class="card card-back" aria-label="Business card back">
    <div class="back-band"></div>

    <div class="contact">
      <p class="contact-item">T 000.123.9876<br>M 666.956.2376</p>
      <p class="contact-item">Your street address<br>will be here</p>
      <p class="contact-item">mailid@serviceholder.com</p>
    </div>

    <div class="contact-icons">
      <span class="contact-icon">
        <svg viewBox="0 0 24 24" aria-hidden="true"><path d="M6.6 10.8a15.2 15.2 0 0 0 6.6 6.6l2.2-2.2a1 1 0 0 1 1-.25 11.4 11.4 0 0 0 3.6.57 1 1 0 0 1 1 1V20a1 1 0 0 1-1 1A17 17 0 0 1 3 4a1 1 0 0 1 1-1h3.5a1 1 0 0 1 1 1 11.4 11.4 0 0 0 .57 3.6 1 1 0 0 1-.25 1z"/></svg>
      </span>
      <span class="contact-icon">
        <svg viewBox="0 0 24 24" aria-hidden="true"><path d="M12 3 2 12h3v8h5v-5h4v5h5v-8h3z"/></svg>
      </span>
      <span class="contact-icon">
        <svg viewBox="0 0 24 24" aria-hidden="true"><path d="M3 5h18v14H3z M3 5l9 7 9-7" stroke="#ffffff" stroke-width="1.6" stroke-linejoin="round"/></svg>
      </span>
    </div>

    <div class="person">
      <p class="person-name">PERSON NAME</p>
      <p class="person-role">Designation</p>
    </div>
  </section>

</main>
</body>
</html>
```